Kitchen and cabinet shop needs new website

Benvoe Cabinets is a mid-sized, family run cabinet shop that is in the process of updating it's image after being handed over to the second generation. It's been in the business for almost 30 years and our designers have lots of experience in the design, home building and renovation industry. Our business offers free home consultations or a customer can visit our showroom to start the design process. Whether the client is a designer, home builder or homeowner we can help create the kitchen and space you're after by helping every step of the way.

The website needs to showcase our past work, (pictures to be included), show the different styles (eg. traditional, modern) and different areas of the home we can produce cabinets for. We created a new logo with Sketch hive that needs to be included in the website as well as the colours. I would like 5 pages;
-Home page
-About us
-portfolio/gallery
-services
-contact us

I would like the website to have a contemporary look, nothing too busy or complicated.

I will attach some pictures with the different styles of our work I mentioned above and provide content for each job.
Updates

Target Market(s)

home owners, designer, home builders, business owners

Industry/Entity Type

Home Builder

Number of Pages Required

5+ page

Font styles to use
Sans Serif

Requirements
Must have
• home page, about us page, gallery/portfolio page-showing various pictures of our work and different styles, services page and contact us.
• Use logo and similar colours as in logo for the scheme
• more content and pictures to follow...

```html
<!DOCTYPE html>
<html lang="en">
<head>
<meta charset="utf-8">
<title>Benvoe Cabinets – Home</title>
<link href="https://fonts.googleapis.com/css2?family=Arimo:wght@400;700&display=swap" rel="stylesheet">
<style>
  :root {
    --orange: #f47920;
    --blue-deep: #3f6dc8;
    --blue-pale: #b3c0fb;
    --logo-blue: #1f5fae;
    --white: #ffffff;
    --ink: #000000;
    --quote-bg: #aaaaaa;
    --quote-ink: #11113a;
    --footer-ink: #e4e8f8;
  }
  * { margin: 0; padding: 0; box-sizing: border-box; }
  html, body { width: 1200px; height: 900px; overflow: hidden; }
  body {
    position: relative;
    background: var(--white);
    font-family: "Arimo", Arial, sans-serif;
    color: var(--ink);
  }
  .top-band { position: absolute; left: 99px; top: 0; width: 1002px; height: 15px; background: var(--orange); }
  .brand { position: absolute; left: 108px; top: 36px; display: flex; align-items: center; gap: 12px; }
  .brand-mark { width: 52px; height: 52px; background: var(--logo-blue); }
  .brand-name { font-size: 38px; font-weight: 700; color: var(--logo-blue); letter-spacing: 1px; }
  .main-nav {
    position: absolute; left: 100px; top: 116px; width: 1001px; height: 34px;
    background: var(--orange); display: flex; align-items: center; padding-left: 8px;
  }
  .main-nav a {
    color: var(--white); text-decoration: none; font-weight: 700; font-size: 14px;
    padding: 0 12px; border-left: 3px solid var(--white); line-height: 17px;
  }
  .main-nav a:first-child { border-left: none; padding-left: 0; padding-right: 14px; color: #f6e7f5; }
  .main-nav a.contact { border-left: none; margin-top: 6px; }
  .page-area { position: absolute; left: 0; top: 150px; width: 1200px; height: 650px; background: var(--blue-pale); }
  .content-panel {
    position: absolute; left: 96px; top: 156px; width: 700px; height: 622px;
    background: var(--white); padding: 14px 0 0 6px;
  }
  .content-panel h1 { font-size: 28px; font-weight: 700; margin: 0 0 11px 1px; line-height: 30px; }
  .content-panel p { font-size: 13.6px; line-height: 15px; margin-bottom: 15px; padding-right: 2px; }
  .feature-photo {
    float: right; width: 400px; height: 260px; margin: 0 0 4px 4px;
    background: linear-gradient(160deg, #e9e4dc 0%, #b9aea0 45%, #6a5140 80%, #4a3323 100%);
  }
  .sidebar {
    position: absolute; left: 801px; top: 158px; width: 300px; height: 620px;
    background: var(--white); padding: 6px 0 0 5px;
  }
  .search-box {
    display: block; margin-left: 7px; width: 88px; height: 15px;
    border: 1px solid #555; font-size: 8px; padding-left: 2px; line-height: 13px; color: #333;
  }
  .sidebar h2 { font-size: 16px; font-weight: 700; margin: 14px 0 7px 1px; }
  .testimonial { margin-bottom: 10px; }
  .testimonial blockquote {
    background: var(--quote-bg); color: var(--quote-ink); font-size: 14px; line-height: 16px;
    padding: 1px 2px 7px 2px;
  }
  .testimonial cite { display: block; text-align: right; font-style: normal; font-size: 14px; color: var(--quote-ink); margin-top: 5px; padding-right: 4px; }
  .testimonial.second { margin-left: -2px; }
  .testimonial.second blockquote { padding-bottom: 2px; }
  .testimonial.second cite { padding-right: 0; margin-top: 4px; }
  .site-footer {
    position: absolute; left: 0; top: 800px; width: 1200px; height: 100px; background: var(--blue-deep);
    color: var(--footer-ink); font-size: 13.5px; line-height: 16px; padding: 14px 0 0 755px;
  }
</style>
</head>
<body>
  <div class="top-band"></div>
  <header class="brand">
    <span class="brand-mark"></span>
    <span class="brand-name">Benvoe Cabinets</span>
  </header>
  <nav class="main-nav">
    <a href="#">Home</a>
    <a href="#">About</a>
    <a href="#">Gallery</a>
    <a href="#">Services</a>
    <a href="#">Testimonials</a>
    <a href="#" class="contact">Contact Us</a>
  </nav>
  <div class="page-area"></div>
  <main class="content-panel">
    <h1>Home</h1>
    <div class="feature-photo" role="img" aria-label="Photo of a bright custom kitchen with white cabinets, island and bar stools"></div>
    <p>Lorem ipsum dolor sit amet, consectetur adipiscing elit. Aliquam id ipsum justo. Duis rutrum rhoncus massa vitae malesuada. Pellentesque consequat neque non mattis lobortis. Proin venenatis eget ante id semper. Praesent et convallis quam, sit amet imperdiet &nbsp;risus. Fusce at sodales nunc, ut ultricies neque. Vestibulum at neque lorem. Suspendisse vitae diam congue, ullamcorper leo finibus, varius lacus. Pellentesque mauris felis, fermentum in pretium non, pulvinar et nulla. Sed convallis sit amet ligula a pulvinar. In non pretium augue. Vivamus ut eros placerat, ultrices velit id, placerat eros.</p>
    <p>Vivamus sit amet metus lobortis, luctus nunc sed, porta turpis. Nunc at magna sagittis ex dignissim tempor. Curabitur tempus eros sapien, at vestibulum nunc blandit feugiat. Duis tempus risus sem. Nullam imperdiet, diam sed efficitur vestibulum, purus justo dapibus arcu, at posuere diam libero eu lectus. In at turpis vitae dui ultricies vestibulum eget tincidunt quam. Maecenas vel erat quam. Aliquam a feugiat ipsum. Maecenas bibendum lacus tellus, sed consectetur purus bibendum in. Proin non arcu ut enim commodo placerat vitae a sem. Sed vestibulum leo elit.</p>
  </main>
  <aside class="sidebar">
    <span class="search-box">Looking For</span>
    <h2>Testimonials</h2>
    <div class="testimonial">
      <blockquote>The cabinets Benvoe made were absolutely amazing! Working with them was a dream, their staff were all so professional and friendly. I would recommend them to anyone.</blockquote>
      <cite>John Doe</cite>
    </div>
    <div class="testimonial second">
      <blockquote>I'm just loving thier work, it's exactly what I was looking for! The cabinets fit the design of my kitchen perfectly!</blockquote>
      <cite>Jane Person</cite>
    </div>
  </aside>
  <footer class="site-footer">
    (c) 2015 Benvoe Custom Cabinets Ltd, All rights reserved.
  </footer>
</body>
</html>
```